Maple construction of ny Roofing flyer

We would like to create a flyer for roofing customers : commercial / real estate management / business / schools /warehouses

Flat roof specialists
Waterproofing experts

Special flat roof re layer @ 3.00 per sq ft

Roof leak repairs
Flashing
Waterproofing

Call 555 2719364

For pictures find torch down roof applications
Flat roofs ny

```html
<!DOCTYPE html>
<html lang="en">
<head>
<meta charset="utf-8">
<title>Maple Construction of NY Roofing Flyer</title>
<link href="https://fonts.googleapis.com/css2?family=Figtree:wght@700;800;900&family=Playfair+Display:wght@400;700;900&display=swap" rel="stylesheet">
<style>
  :root {
    --navy: #1b2a78;
    --sky-blue: #16a2e2;
    --red: #cf1126;
    --red-dark: #9e0b1c;
    --ink: #2e2e2e;
    --white: #ffffff;
    --page-bg: #a3a3a3;
  }
  * { margin: 0; padding: 0; box-sizing: border-box; }
  html, body {
    width: 1200px; height: 2196px; overflow: hidden;
    background: var(--page-bg);
  }
  .stage { position: relative; width: 1200px; height: 2196px; }
  .flyer {
    position: absolute; left: 100px; top: 391px;
    width: 874px; height: 1236px;
    transform: scale(1.1442); transform-origin: top left;
    background: var(--white); overflow: hidden;
    box-shadow: 0 6px 18px rgba(0,0,0,.35);
    font-family: "Figtree", sans-serif;
  }
  .flyer-art { position: absolute; inset: 0; width: 874px; height: 1236px; }
  .headline {
    position: absolute; left: 36px; top: 40px;
    font-family: "Playfair Display", serif; font-weight: 700;
    font-size: 100px; line-height: 97px; color: var(--navy);
    letter-spacing: -1px;
  }
  .company-name {
    position: absolute; left: 505px; top: 46px; width: 345px;
    font-family: "Playfair Display", serif; font-weight: 400;
    font-size: 36px; line-height: 46px; color: #3a3a3a;
    white-space: nowrap;
  }
  .offer-badge {
    position: absolute; left: 605px; top: 532px; width: 236px; height: 236px;
    color: var(--white); text-align: center; font-weight: 800;
  }
  .offer-title { position: absolute; top: 30px; width: 100%; font-size: 25px; line-height: 25px; }
  .offer-price { position: absolute; top: 108px; width: 100%; font-size: 60px; line-height: 70px; font-weight: 900; }
  .offer-unit { position: absolute; top: 182px; width: 100%; font-size: 23px; }
  .specialties {
    position: absolute; left: 0; top: 780px; width: 100%; text-align: center;
    font-weight: 900; font-size: 54px; line-height: 58px; letter-spacing: -.5px;
  }
  .specialties .line-one { color: var(--sky-blue); }
  .specialties .line-two { color: var(--navy); }
  .service { position: absolute; width: 220px; text-align: center; font-weight: 800; font-size: 25px; line-height: 33px; color: var(--ink); }
  .service svg { display: block; margin: 0 auto 8px; }
  .service-leak { left: 91px; top: 928px; }
  .service-flashing { left: 332px; top: 918px; }
  .service-waterproofing { left: 567px; top: 925px; }
  .contact-note {
    position: absolute; left: 0; top: 1080px; width: 100%; height: 38px;
    display: flex; align-items: center; justify-content: center; gap: 18px;
    color: var(--white); font-weight: 800; font-size: 22px;
  }
  .contact-note .rule { width: 58px; height: 2px; background: var(--white); }
  .call-line {
    position: absolute; left: 0; top: 1120px; width: 100%; text-align: center;
    color: var(--white); font-weight: 800; font-size: 56px; line-height: 72px;
    display: flex; align-items: center; justify-content: center; gap: 22px;
  }
  .web-line {
    position: absolute; left: 0; top: 1188px; width: 100%;
    display: flex; align-items: center; justify-content: center; gap: 14px;
    color: var(--white); font-weight: 800; font-size: 23px;
  }
</style>
</head>
<body>
<div class="stage">
  <div class="flyer">
    <svg class="flyer-art" viewBox="0 0 874 1236">
      <defs>
        <linearGradient id="skyTone" x1="0" y1="0" x2="0" y2="1">
          <stop offset="0" stop-color="#e9edf2"/>
          <stop offset=".35" stop-color="#dfe4ea"/>
          <stop offset=".6" stop-color="#aeb5bd"/>
          <stop offset="1" stop-color="#5d646d"/>
        </linearGradient>
        <radialGradient id="roofShade" cx=".05" cy=".95" r=".6">
          <stop offset="0" stop-color="#4a4f57" stop-opacity=".95"/>
          <stop offset="1" stop-color="#4a4f57" stop-opacity="0"/>
        </radialGradient>
        <radialGradient id="workerTone" cx=".9" cy=".6" r=".45">
          <stop offset="0" stop-color="#2b3f66" stop-opacity=".85"/>
          <stop offset=".6" stop-color="#6a7c96" stop-opacity=".35"/>
          <stop offset="1" stop-color="#6a7c96" stop-opacity="0"/>
        </radialGradient>
        <radialGradient id="badgeRed" cx=".4" cy=".3" r=".8">
          <stop offset="0" stop-color="#e0142c"/>
          <stop offset="1" stop-color="#9e0b1c"/>
        </radialGradient>
        <clipPath id="badgeClip"><circle cx="723" cy="650" r="116"/></clipPath>
      </defs>
      <g role="img" aria-label="Photo of two roofers in hard hats nailing shingles on a roof under a cloudy sky">
        <rect x="0" y="0" width="874" height="790" fill="url(#skyTone)"/>
        <rect x="0" y="0" width="874" height="790" fill="url(#roofShade)"/>
        <rect x="0" y="0" width="874" height="790" fill="url(#workerTone)"/>
      </g>
      <path d="M0,620 C170,730 420,772 640,742 L874,596 L874,1236 L0,1236 Z" fill="var(--sky-blue)"/>
      <path d="M0,636 C170,746 420,788 640,758 L874,612 L874,1236 L0,1236 Z" fill="var(--white)"/>
      <circle cx="723" cy="650" r="128" fill="var(--white)"/>
      <circle cx="723" cy="650" r="116" fill="url(#badgeRed)"/>
      <rect x="600" y="640" width="250" height="70" fill="#1a1a1a" clip-path="url(#badgeClip)"/>
      <rect x="0" y="1080" width="874" height="40" fill="var(--sky-blue)"/>
      <rect x="0" y="1118" width="874" height="118" fill="var(--navy)"/>
      <line x1="326" y1="965" x2="326" y2="1050" stroke="#333" stroke-width="2"/>
      <line x1="571" y1="965" x2="571" y2="1050" stroke="#333" stroke-width="2"/>
    </svg>

    <h1 class="headline">Need A<br>Roofing<br>Experts?</h1>
    <p class="company-name">Maple Construction<br>OF NY Roofing</p>

    <div class="offer-badge">
      <div class="offer-title">SPECIAL<br>FLAT ROOF<br>RE LAYER</div>
      <div class="offer-price">@3.00</div>
      <div class="offer-unit">per sq/ft</div>
    </div>

    <div class="specialties">
      <div class="line-one">FLAT ROOF SPECIALISTS</div>
      <div class="line-two">WATERPROOFING EXPERTS</div>
    </div>

    <div class="service service-leak">
      <svg width="60" height="44" viewBox="0 0 60 44"><path d="M4,22 L30,4 L56,22" fill="none" stroke="var(--red)" stroke-width="6" stroke-linejoin="round"/><path d="M12,20 V38" stroke="var(--red)" stroke-width="5"/><path d="M42,24 c-4,6 -5,9 -5,11 a5,5 0 0 0 10,0 c0,-2 -1,-5 -5,-11z" fill="var(--red)"/></svg>
      ROOF LEAK<br>REPAIRS
    </div>
    <div class="service service-flashing">
      <svg width="70" height="70" viewBox="0 0 70 70"><g stroke="var(--red)" stroke-width="2.5" stroke-dasharray="5 5" fill="none"><circle cx="35" cy="35" r="30"/></g><path d="M39,14 L24,38 H34 L30,56 L46,30 H36 Z" fill="var(--red)"/></svg>
      FLASHING
    </div>
    <div class="service service-waterproofing">
      <svg width="60" height="66" viewBox="0 0 60 66"><path d="M30,3 L55,12 V32 C55,48 44,58 30,63 C16,58 5,48 5,32 V12 Z" fill="none" stroke="var(--red)" stroke-width="4"/><path d="M30,18 c-7,10 -10,15 -10,19 a10,10 0 0 0 20,0 c0,-4 -3,-9 -10,-19z" fill="var(--red)"/></svg>
      WATER<br>PROOFING
    </div>

    <div class="contact-note"><span class="rule"></span>FOR MORE INFORMATION, PLEASE CONTACT US TODAY<span class="rule"></span></div>
    <div class="call-line">
      <svg width="38" height="38" viewBox="0 0 38 38"><rect x="1" y="1" width="36" height="36" rx="6" fill="var(--white)"/><path d="M12,8 l5,0 2,7 -3,2 c1,4 3,7 7,9 l2,-3 7,2 0,5 c-12,1 -20,-8 -20,-22z" fill="var(--navy)"/></svg>
      <span>CALL US :&nbsp; 555 2719 364</span>
    </div>
    <div class="web-line">
      <svg width="22" height="22" viewBox="0 0 22 22" fill="none" stroke="var(--white)" stroke-width="1.6"><circle cx="11" cy="11" r="9"/><ellipse cx="11" cy="11" rx="4" ry="9"/><line x1="2" y1="11" x2="20" y2="11"/></svg>
      <span>VISIT : WWW.MAPLEROOFINGNY.COM</span>
    </div>
  </div>
</div>
</body>
</html>
```